Web Application Graphic Design Project

We need a design for an online literacy application. The target audience are 9-12 year old children and the application will teach them literacy skills, like essay writing. It is a web-based application called Lumorival and the software developers now need a graphic design to implement into the code - no coding required, just design of the layout.
Wireframes are attached to give an overview of what the functionalities are - it runs in any ordinary web-browser (indicated in the wireframes as well). The application consists of a static background (workspace) onto which individual boxes are added as the student progresses through the tasks. A task panel on the left hand side allows the user to select a task, upon which a popup window will slide open on the right where they enter content. This content is then displayed on the workspace in the background in a box (which can be moved around to organise, seen in frame 3 ). Additional icons on left and right lead to new tasks.
Updates
The wireframe mockup of the application has been updated - please ignore the previous one, which has now been deleted. This is the final version to work from.
Reason: Would like to give more time to allow for a design that meets the young children target audience and for more creative ways for icons and colour schemes.
Reason: We are waiting for some further submissions to come through.
Target Market(s)
9-12 year old school children, so the design should be appealing to both boys and girls.
Industry/Entity Type
Graphic Design
Look and feel
Each slider illustrates characteristics of the customer's brand and the style your logo design should communicate.

```html
<!DOCTYPE html>
<html lang="en">
<head>
<meta charset="utf-8">
<title>Lumorival – Essay Writing Workspace</title>
<link href="https://fonts.googleapis.com/css2?family=Arimo:wght@400;700&display=swap" rel="stylesheet">
<style>
  :root {
    --bar-green-top: #3a8a6b;
    --bar-green-bottom: #1d5c45;
    --wood: #f2a623;
    --wood-dark: #c9801a;
    --paper: #fdf5c2;
    --paper-line: #b9cad9;
    --margin-line: #eaa89a;
    --board-dark: #15332a;
    --board-mid: #2b6a55;
    --board-light: #3d826a;
    --chalk: #ffffff;
    --done: #f4a12a;
    --newbie: #b3236e;
    --developer: #a7c63a;
    --star: #f2a623;
    --card: #ffffff;
    --card-line: #c6d3e6;
    --card-title: #d6362b;
    --card-text: #2a2a3a;
    --icon-navy: #1e3150;
    --brand: #a6c43b;
    --ink: #1c1c1c;
  }
  * { box-sizing: border-box; margin: 0; padding: 0; }
  html, body { width: 1200px; height: 927px; overflow: hidden; }
  body {
    position: relative;
    font-family: "Arimo", Arial, sans-serif;
    background:
      linear-gradient(90deg, transparent 178px, var(--margin-line) 178px, var(--margin-line) 181px, transparent 181px, transparent 187px, var(--margin-line) 187px, var(--margin-line) 190px, transparent 190px),
      repeating-linear-gradient(180deg, transparent 0, transparent 30px, var(--paper-line) 30px, var(--paper-line) 32px),
      var(--paper);
    background-position: 0 0, 0 150px, 0 0;
  }

  /* Browser bar */
  .browser-bar {
    position: absolute; left: 0; top: 0; width: 1200px; height: 146px;
    background: linear-gradient(180deg, var(--bar-green-top), var(--bar-green-bottom));
    border-top: 6px solid var(--wood);
    border-bottom: 12px solid var(--wood);
  }
  .browser-bar .site-line {
    position: absolute; top: 20px; width: 100%; text-align: center;
    color: var(--chalk); font-size: 20px;
  }
  .nav-icon { position: absolute; top: 52px; }
  .address-field {
    position: absolute; left: 376px; top: 53px; width: 604px; height: 47px;
    background: #fff; border-radius: 4px;
  }
  .search-field {
    position: absolute; left: 995px; top: 52px; width: 183px; height: 48px;
    background: #fff; border-radius: 14px;
  }
  .search-field svg { position: absolute; left: 8px; top: 6px; }

  /* Left tool icons */
  .tool {
    position: absolute; width: 110px; text-align: center;
    font-size: 20px; color: var(--ink);
  }
  .tool svg { display: block; margin: 0 auto 6px; }

  /* Task panel */
  .task-panel {
    position: absolute; left: 106px; top: 170px; width: 270px; height: 698px;
    background: var(--board-dark);
    border-top: 16px solid var(--wood);
    border-bottom: 16px solid var(--wood);
    box-shadow: 0 2px 0 var(--wood-dark);
  }
  .levels {
    position: absolute; left: 0; top: 0; width: 100%; height: 102px;
    display: flex; justify-content: space-between; padding: 6px 8px 0 10px;
  }
  .level { text-align: center; font-size: 19px; }
  .level .badge { display: block; margin: 0 auto 4px; height: 50px; border-radius: 14px; }
  .level-newbie { color: var(--newbie); }
  .level-newbie .badge { width: 46px; background: var(--newbie); }
  .level-developer { color: var(--developer); }
  .level-developer .badge { width: 48px; background: var(--developer); }
  .level-star { color: var(--star); }
  .level-star .badge { width: 40px; background: var(--star); border-radius: 50%; height: 44px; margin-top: 6px; }

  .board {
    position: absolute; left: 0; top: 116px; width: 270px; height: 520px;
    background: radial-gradient(ellipse at 45% 25%, var(--board-light), var(--board-mid) 60%, #1f5646);
    border: 4px solid #0f2a22;
    padding: 16px 14px;
  }
  .board h2 {
    color: var(--chalk); font-size: 19px; font-weight: 700; letter-spacing: 6px;
    margin-bottom: 6px;
  }
  .steps { list-style: none; }
  .steps li {
    position: relative; color: var(--chalk); font-size: 19px; line-height: 27px;
  }
  .steps li.done { color: var(--done); }
  .steps li.done svg { position: absolute; right: 2px; top: 2px; }

  /* Workspace cards */
  .note-card {
    position: absolute; background-color: var(--card);
    background-image:
      linear-gradient(90deg, transparent 40px, var(--card-title) 40px, var(--card-title) 42px, transparent 42px),
      repeating-linear-gradient(180deg, transparent 0, transparent 14px, var(--card-line) 14px, var(--card-line) 15px);
    background-position: 0 0, 0 60px;
    background-repeat: no-repeat, repeat;
    background-size: auto, 100% calc(100% - 60px);
    box-shadow: 2px 4px 8px rgba(0,0,0,.35);
  }
  .note-card::before {
    content: ""; position: absolute; left: 12px; top: 38px; width: 11px; height: 11px;
    border-radius: 50%; background: #e6e4d4; box-shadow: inset 1px 1px 2px rgba(0,0,0,.3);
  }
  .note-card h3 {
    position: absolute; left: 60px; top: 36px;
    color: var(--card-title); font-weight: 400; font-size: 16.5px;
  }
  .note-card p { position: absolute; left: 60px; color: var(--card-text); font-size: 16px; }
  .card-question { left: 394px; top: 182px; width: 333px; height: 204px; }
  .card-question p { top: 84px; line-height: 32px; width: 265px; }
  .card-decode { left: 545px; top: 361px; width: 334px; height: 203px; }
  .card-decode p { top: 93px; line-height: 21px; }
  .card-ideas { left: 621px; top: 533px; width: 334px; height: 293px; }
  .card-ideas h3 { left: 65px; }
  .card-ideas p { left: 65px; top: 98px; line-height: 22px; width: 210px; }

  /* Brand */
  .brand {
    position: absolute; left: 900px; top: 162px;
    font-size: 34px; font-weight: 700; color: var(--brand); letter-spacing: 1px;
  }

  /* Right menu */
  .menu-item {
    position: absolute; left: 1070px; width: 112px; text-align: center;
    font-size: 20px; color: var(--ink);
  }
  .menu-item svg { display: block; margin: 0 auto 4px; }
</style>
</head>
<body>

<header class="browser-bar">
  <div class="site-line">Lumorival.com.au Copyright 2012</div>
  <svg class="nav-icon" style="left:12px" width="68" height="58" viewBox="0 0 68 58" aria-label="Back">
    <path d="M4 29 L30 4 L30 18 L64 18 L64 40 L30 40 L30 54 Z" fill="#e9f1ea"/>
  </svg>
  <svg class="nav-icon" style="left:92px" width="68" height="58" viewBox="0 0 68 58" aria-label="Forward">
    <path d="M64 29 L38 4 L38 18 L4 18 L4 40 L38 40 L38 54 Z" fill="#e9f1ea"/>
  </svg>
  <svg class="nav-icon" style="left:186px" width="58" height="58" viewBox="0 0 58 58" aria-label="Stop">
    <path d="M6 16 L16 6 L29 19 L42 6 L52 16 L39 29 L52 42 L42 52 L29 39 L16 52 L6 42 L19 29 Z" fill="#e9f1ea"/>
  </svg>
  <svg class="nav-icon" style="left:270px" width="72" height="58" viewBox="0 0 72 58" aria-label="Home">
    <path d="M4 30 L36 4 L68 30 L60 30 L60 56 L44 56 L44 38 L28 38 L28 56 L12 56 L12 30 Z" fill="#e9f1ea"/>
  </svg>
  <div class="address-field"></div>
  <div class="search-field">
    <svg width="40" height="38" viewBox="0 0 40 38" aria-label="Search">
      <circle cx="21" cy="15" r="10" fill="none" stroke="var(--bar-green-bottom)" stroke-width="4"/>
      <path d="M14 22 L4 33" stroke="var(--bar-green-bottom)" stroke-width="6" stroke-linecap="round"/>
    </svg>
  </div>
</header>

<div class="tool" style="left:6px; top:213px">
  <svg width="52" height="50" viewBox="0 0 52 50" aria-hidden="true">
    <path d="M10 40 L40 8 L48 16 L18 46 L6 48 Z" fill="var(--icon-navy)"/>
    <path d="M4 48 L48 48" stroke="var(--icon-navy)" stroke-width="2"/>
  </svg>
  Lesson
</div>
<div class="tool" style="left:3px; top:302px">
  <svg width="34" height="60" viewBox="0 0 34 60" aria-hidden="true">
    <rect x="2" y="2" width="30" height="56" fill="none" stroke="var(--ink)" stroke-width="2"/>
    <path d="M2 20 H32 M2 39 H32" stroke="var(--ink)" stroke-width="2"/>
    <rect x="13" y="9" width="8" height="3" fill="var(--ink)"/>
    <rect x="13" y="27" width="8" height="3" fill="var(--ink)"/>
    <rect x="13" y="46" width="8" height="3" fill="var(--ink)"/>
  </svg>
  Activities
</div>

<aside class="task-panel">
  <div class="levels">
    <div class="level level-newbie"><span class="badge" role="img" aria-label="Teddy bear character for the Newbie level"></span>Newbie</div>
    <div class="level level-developer"><span class="badge" role="img" aria-label="Reading child character for the Developer level"></span>Developer</div>
    <div class="level level-star"><span class="badge" role="img" aria-label="Graduate character for the Star level"></span>Star</div>
  </div>
  <nav class="board">
    <h2>ESSAY WRITING</h2>
    <ul class="steps">
      <li>Overview</li>
      <li class="done">The Question<svg width="24" height="24" viewBox="0 0 24 24" aria-hidden="true"><rect x="2" y="4" width="18" height="18" fill="none" stroke="var(--done)" stroke-width="2"/><path d="M6 12 L11 17 L22 2" fill="none" stroke="var(--done)" stroke-width="3"/></svg></li>
      <li class="done">Decoding the Q<svg width="24" height="24" viewBox="0 0 24 24" aria-hidden="true"><rect x="2" y="4" width="18" height="18" fill="none" stroke="var(--done)" stroke-width="2"/><path d="M6 12 L11 17 L22 2" fill="none" stroke="var(--done)" stroke-width="3"/></svg></li>
      <li class="done">Your Ideas<svg width="24" height="24" viewBox="0 0 24 24" aria-hidden="true"><rect x="2" y="4" width="18" height="18" fill="none" stroke="var(--done)" stroke-width="2"/><path d="M6 12 L11 17 L22 2" fill="none" stroke="var(--done)" stroke-width="3"/></svg></li>
      <li>Structure</li>
      <li>Writing</li>
      <li>Review</li>
    </ul>
  </nav>
</aside>

<section class="note-card card-question">
  <h3>Teacher-Set Question</h3>
  <p>How has the internet changed our perception of the nature of information?</p>
</section>
<section class="note-card card-decode">
  <h3>Decoding The Question</h3>
  <p>Opinion - How?<br>Research Perceptions<br>Facts Information</p>
</section>
<section class="note-card card-ideas">
  <h3>Decoding The Question</h3>
  <p>- Quality - better information, more current<br>- Quality - more Information<br>- Search - finding information is easy</p>
</section>

<div class="brand">Lumorival</div>

<div class="menu-item" style="top:158px">
  <svg width="30" height="54" viewBox="0 0 30 54" aria-hidden="true">
    <circle cx="15" cy="7" r="7" fill="var(--icon-navy)"/>
    <path d="M4 16 H26 V34 H22 V54 H17 V36 H13 V54 H8 V34 H4 Z" fill="var(--icon-navy)"/>
  </svg>
  Name
</div>
<div class="menu-item" style="top:252px">
  <svg width="40" height="50" viewBox="0 0 40 50" aria-hidden="true">
    <path d="M4 10 L16 2 L22 28 L10 36 Z" fill="none" stroke="var(--icon-navy)" stroke-width="2"/>
    <path d="M10 12 L22 6 L26 30 L14 36 Z" fill="#fff" stroke="var(--icon-navy)" stroke-width="2"/>
    <rect x="18" y="26" width="20" height="22" fill="var(--icon-navy)"/>
    <rect x="6" y="36" width="14" height="12" fill="var(--icon-navy)"/>
  </svg>
  Reference
</div>
<div class="menu-item" style="top:346px">
  <svg width="38" height="50" viewBox="0 0 38 50" aria-hidden="true">
    <path d="M2 2 H26 L36 12 V48 H2 Z" fill="#fff" stroke="var(--icon-navy)" stroke-width="3"/>
    <path d="M8 18 H30 M8 25 H30 M8 32 H30 M8 39 H30" stroke="var(--icon-navy)" stroke-width="3"/>
  </svg>
  Samples
</div>
<div class="menu-item" style="top:440px">
  <svg width="46" height="46" viewBox="0 0 46 46" aria-hidden="true">
    <rect x="2" y="2" width="42" height="42" fill="none" stroke="var(--icon-navy)" stroke-width="3"/>
    <rect x="10" y="2" width="26" height="14" fill="none" stroke="var(--icon-navy)" stroke-width="3"/>
    <rect x="8" y="24" width="30" height="20" fill="var(--icon-navy)"/>
  </svg>
  Save
</div>
<div class="menu-item" style="top:525px">
  <svg width="54" height="50" viewBox="0 0 54 50" aria-hidden="true">
    <rect x="2" y="2" width="50" height="12" rx="6" fill="var(--icon-navy)"/><circle cx="44" cy="8" r="5" fill="#fff"/>
    <rect x="2" y="19" width="50" height="12" rx="6" fill="var(--icon-navy)"/><circle cx="44" cy="25" r="5" fill="#fff"/>
    <rect x="2" y="36" width="50" height="12" rx="6" fill="none" stroke="var(--icon-navy)" stroke-width="2"/><circle cx="10" cy="42" r="5" fill="var(--icon-navy)"/>
  </svg>
  Settings
</div>
<div class="menu-item" style="top:612px">
  <svg width="40" height="64" viewBox="0 0 40 64" aria-hidden="true">
    <rect x="2" y="2" width="36" height="60" fill="none" stroke="var(--icon-navy)" stroke-width="3"/>
    <path d="M4 4 L26 12 V62 L4 60 Z" fill="var(--icon-navy)"/>
  </svg>
  Exit
</div>

</body>
</html>
```